Corvanta512 Business Card Redesign

I want to create a design for brand new business cards, I need something exceptional for clear plastic business card design. Please do not submit without it being on a clear design. Photos of the various logo versions attached.

```html
<!DOCTYPE html>
<html lang="en">
<head>
<meta charset="utf-8">
<title>Corvanta512 Business Card</title>
<link href="https://fonts.googleapis.com/css2?family=Montserrat:wght@400;500;700&display=swap" rel="stylesheet">
<style>
  :root {
    --page-bg: #e9e6e1;
    --card-top: #f3efe9;
    --card-mid: #e6dccd;
    --card-cool: #dfe7ee;
    --card-edge: #ffffff;
    --navy: #1f2a48;
    --ink: #1d1d22;
    --gold: #b8953f;
    --gold-faint: rgba(184, 149, 63, 0.14);
  }
  * { margin: 0; padding: 0; box-sizing: border-box; }
  html, body {
    width: 1200px;
    height: 1091px;
    overflow: hidden;
    background: var(--page-bg);
    font-family: "Montserrat", sans-serif;
  }
  .card {
    position: absolute;
    left: 60px;
    top: 236px;
    width: 1080px;
    height: 618px;
    border-radius: 27px;
    border: 2px solid var(--card-edge);
    background:
      radial-gradient(ellipse 260px 420px at 560px 260px, rgba(223, 231, 238, 0.9), transparent 70%),
      linear-gradient(100deg, var(--card-top) 0%, var(--card-mid) 45%, var(--card-cool) 62%, var(--card-mid) 100%);
    box-shadow: 0 18px 40px rgba(0, 0, 0, 0.12);
    overflow: hidden;
  }
  .brand-mark {
    position: absolute;
    left: 120px;
    top: 50px;
    width: 160px;
    height: 160px;
    border-radius: 50%;
    background: var(--gold);
  }
  .brand-name {
    position: absolute;
    left: 44px;
    top: 238px;
    font-size: 44px;
    font-weight: 700;
    color: var(--gold);
    letter-spacing: 0.5px;
  }
  .backdrop-circle {
    position: absolute;
    left: 720px;
    top: 200px;
    width: 390px;
    height: 390px;
    border-radius: 50%;
    background: var(--gold-faint);
  }
  .person {
    position: absolute;
    right: 35px;
    top: 66px;
    text-align: right;
  }
  .person-name {
    font-size: 40px;
    font-weight: 700;
    color: var(--navy);
    letter-spacing: 0.3px;
  }
  .person-role {
    margin-top: 8px;
    font-size: 25px;
    font-weight: 500;
    color: var(--ink);
  }
  .address {
    position: absolute;
    left: 37px;
    top: 350px;
    font-size: 27px;
    font-weight: 500;
    line-height: 45px;
    color: var(--ink);
  }
  .contacts {
    position: absolute;
    left: 38px;
    top: 458px;
    list-style: none;
  }
  .contact-item {
    display: flex;
    align-items: center;
    height: 46px;
    font-size: 28px;
    font-weight: 500;
    color: var(--ink);
  }
  .contact-icon {
    width: 28px;
    height: 28px;
    margin-right: 14px;
    fill: var(--navy);
  }
</style>
</head>
<body>
  <div class="card">
    <div class="backdrop-circle"></div>

    <div class="brand-mark"></div>
    <div class="brand-name">Corvanta512</div>

    <div class="person">
      <div class="person-name">MARCUS DELANEY</div>
      <div class="person-role">Founder &amp; CEO</div>
    </div>

    <div class="address">
      482 Linden Ave, Suite 310<br>
      Fairhaven, CA 90418
    </div>

    <ul class="contacts">
      <li class="contact-item">
        <svg class="contact-icon" viewBox="0 0 24 24" aria-hidden="true"><path d="M6.6 10.8a15 15 0 0 0 6.6 6.6l2.2-2.2a1 1 0 0 1 1-.25 11.4 11.4 0 0 0 3.6.57 1 1 0 0 1 1 1V20a1 1 0 0 1-1 1A17 17 0 0 1 3 4a1 1 0 0 1 1-1h3.5a1 1 0 0 1 1 1c0 1.25.2 2.45.57 3.57a1 1 0 0 1-.25 1z"/></svg>
        061 4827 3950
      </li>
      <li class="contact-item">
        <svg class="contact-icon" viewBox="0 0 24 24" aria-hidden="true"><path d="M2 5h20v14H2z M3.5 6.5 12 13l8.5-6.5" fill="none" stroke="currentColor"/><path d="M2 5h20v2l-10 7L2 7z M2 8.5l6.5 4.5L2 18z M22 8.5 15.5 13 22 18z M9.8 14l2.2 1.5 2.2-1.5L22 19H2z"/></svg>
        info@corvanta512.com
      </li>
      <li class="contact-item">
        <svg class="contact-icon" viewBox="0 0 24 24" aria-hidden="true"><circle cx="12" cy="12" r="10"/><path d="M7 7c2 0 3 1 3 2.5S8 12 9 13.5s3 1 3 3-1 3-1 3M15 5c0 2 2 2 2 4s2 1 3 1" fill="none" stroke="#e6dccd" stroke-width="1.6"/></svg>
        www.corvanta512.com
      </li>
    </ul>
  </div>
</body>
</html>
```